Creative, fresh business card design for Orrin Linings

We need a fresh, creative business card design for Orrin Linings. We are the manufacturer of Orrin Linings in Australia. Wall panels are 2400 x 1200mm panels made from MDF and feature 3D patterns on the face of the panel. The colours to be used are green, silver/grey and white RGB
Red 187
Green 207
Blue 65.

An idea is to possibly use a watermark of one of our designs as a background (like on the "Ferns" design on the left hand side of page 2 of our brochure).

Target Market(s)

Interior designers, architects, builders and home renovators

Industry/Entity Type

Business

Contact Information for Business Card

Details to go on the card are:
Our logo (attached),
Slogan: "Decorative panels for interiors and exteriors",
Contact name,
Position,
Mobile phone number,
Business address,
Business phone,
Business fax,
Website and
Email address.

I have attached a few images of our panels and our brochure for reference.

The colours of the business card should feature our logo colours which are: RGB
Red 187
Green 207
Blue 65

Requirements
Must have
• Very modern fonts and design. Some of the designs shown especially the "Weave" design which is a popular design.
Nice to have
• Creative but simple design. Very contemporary.
Should not have
• Anything ornate or old fashioned.

```html
<!DOCTYPE html>
<html lang="en">
<head>
<meta charset="utf-8">
<title>Orrin Linings – Business Card</title>
<link rel="stylesheet" href="https://fonts.googleapis.com/css2?family=Montserrat:wght@400;500;700;800&display=swap">
<style>
  :root {
    --brand-green: rgb(187, 207, 65);
    --silver: #8d8e91;
    --ink: #4a4a4c;
    --paper: #ffffff;
    --backdrop: #eceded;
    --rule: #6d6e70;
  }
  * { box-sizing: border-box; margin: 0; padding: 0; }
  html, body { width: 1200px; height: 840px; overflow: hidden; }
  body {
    background: var(--backdrop);
    font-family: "Montserrat", Arial, sans-serif;
    color: var(--ink);
    position: relative;
  }
  .card {
    position: absolute;
    left: 180px; top: 180px;
    width: 840px; height: 480px;
    background: var(--paper);
    overflow: hidden;
    box-shadow: 0 2px 6px rgba(0,0,0,0.08);
  }
  .card-base { position: absolute; left: 0; top: 0; width: 840px; height: 480px; }

  .brand {
    position: absolute;
    left: 70px; top: 130px;
    width: 250px;
  }
  .brand-square {
    width: 130px; height: 110px;
    background: var(--brand-green);
    margin-bottom: 16px;
  }
  .brand-name {
    font-weight: 500;
    font-size: 30px;
    color: var(--silver);
    letter-spacing: 0.2px;
    line-height: 1.1;
  }
  .slogan {
    margin-top: 10px;
    font-size: 13px;
    letter-spacing: 2.4px;
    color: var(--silver);
    line-height: 1.35;
  }

  .divider {
    position: absolute;
    left: 345px; top: 70px;
    width: 2px; height: 215px;
    background: var(--rule);
  }

  .contact {
    position: absolute;
    left: 385px; top: 62px;
  }
  .person-name {
    font-weight: 800;
    font-size: 30px;
    color: var(--ink);
    letter-spacing: 0.5px;
    line-height: 1;
  }
  .person-role {
    font-size: 21px;
    color: var(--ink);
    margin: 4px 0 14px 6px;
  }
  .details { list-style: none; margin-left: 22px; }
  .details li {
    display: flex; align-items: flex-start;
    font-size: 18px; line-height: 24px;
    color: var(--ink);
  }
  .details .icon {
    flex: 0 0 18px; width: 18px; height: 18px;
    margin: 3px 10px 0 0;
  }
  .details .icon-gap { flex: 0 0 18px; margin-right: 10px; }
</style>
</head>
<body>
  <div class="card">
    <svg class="card-base" viewBox="0 0 840 480" aria-hidden="true">
      <rect x="0" y="462" width="840" height="18" fill="var(--brand-green)"/>
      <path d="M400 480 V430 Q400 410 420 410 H560 Q580 410 590 396 L600 382 Q606 372 620 372 H840 V480 Z" fill="var(--silver)"/>
    </svg>

    <div class="brand">
      <div class="brand-square"></div>
      <div class="brand-name">Orrin Linings</div>
      <p class="slogan">decorative panels for<br>interiors &amp; landscapes</p>
    </div>

    <div class="divider"></div>

    <div class="contact">
      <h1 class="person-name">ARLEN VOSS</h1>
      <p class="person-role">Manager</p>
      <ul class="details">
        <li>
          <svg class="icon" viewBox="0 0 18 18"><circle cx="9" cy="9" r="9" fill="var(--brand-green)"/><path d="M6 5 L7.6 5 L8.2 7 L7.2 7.8 Q8 9.8 10.2 10.8 L11 9.8 L13 10.4 L13 12 Q12.6 13 11.4 13 Q6.5 12.4 5 6.6 Q5 5.4 6 5 Z" fill="var(--ink)"/></svg>
          12 470 318 2096
        </li>
        <li>
          <svg class="icon" viewBox="0 0 18 18"><circle cx="9" cy="9" r="9" fill="var(--brand-green)"/><rect x="6.5" y="4.5" width="5" height="3" fill="var(--ink)"/><rect x="4.5" y="7.5" width="9" height="4.5" rx="1" fill="var(--ink)"/><rect x="6.5" y="11" width="5" height="2.5" fill="var(--ink)"/></svg>
          12 470 318 2097
        </li>
        <li>
          <svg class="icon" viewBox="0 0 18 18"><circle cx="9" cy="9" r="9" fill="var(--brand-green)"/><circle cx="9" cy="9" r="4.5" fill="none" stroke="var(--ink)" stroke-width="1.2"/><ellipse cx="9" cy="9" rx="2" ry="4.5" fill="none" stroke="var(--ink)" stroke-width="1"/><line x1="4.5" y1="9" x2="13.5" y2="9" stroke="var(--ink)" stroke-width="1"/></svg>
          www.orrinlinings.example
        </li>
        <li>
          <svg class="icon" viewBox="0 0 18 18"><circle cx="9" cy="9" r="9" fill="var(--brand-green)"/><rect x="4.5" y="6" width="9" height="6.5" rx="0.8" fill="var(--ink)"/><path d="M4.8 6.4 L9 9.6 L13.2 6.4" fill="none" stroke="var(--brand-green)" stroke-width="0.9"/></svg>
          arlen@orrinlinings.example
        </li>
        <li>
          <svg class="icon" viewBox="0 0 18 18"><circle cx="9" cy="9" r="9" fill="var(--brand-green)"/><path d="M9 14 Q5.5 9.5 5.5 7.5 A3.5 3.5 0 0 1 12.5 7.5 Q12.5 9.5 9 14 Z" fill="var(--ink)"/><circle cx="9" cy="7.5" r="1.3" fill="var(--brand-green)"/></svg>
          41 Quarry Lane,
        </li>
        <li><span class="icon-gap"></span>Bellmere, VIC 3904</li>
      </ul>
    </div>
  </div>
</body>
</html>
```